Website for Plumbing Company, Tidewell Heating

I need a 7-page fully HTML-coded website for my plumbing company, Tidewell Heating. We specialize in installation, repair, and replacement of both gas and electric water heaters. Although we offer both tankless (on-demand) water heaters and standard (with tank) water heaters, most of our business is related to standard (with tank) water heaters in the USA market.

These are the pages I need:
1. Home page with sections such as About Us, Our Services, Why Choose Us, Testimonials, Location Map (Palm Beach County Florida), Quote Request Form, Join Our Newsletter, Mission Statement, etc.

2. Gas Water Heaters

3. Electric Water Heaters

4. Tankless Water Heaters

5. About Us

6. Contact Us

7. Privacy Policy, Terms & Conditions

Be sure to mention the following points:
1. Same-Day Service
2. Best Price Guarantee
3. 100% Satisfaction Rating
4. 15-Year Warranty on Water Heater & Parts
5. Lifetime Warranty on Workmanship
*All Warranties are Transferrable Upon Home Sale

Once design is selected and finalized, I need the website coded in a standard HTML/CSS and temporarily hosted on your development server so I can see the website functionality that is not observable from screenshots, such as section animations, etc. Once those details are finalized, I will move the source code to my server and complete the project.

Target Market(s)

Residential Home Owners and Business Owners

Industry/Entity Type

Plumbing, Home Services, Remodeling, Construction

Coding

Coded - Design and coding required

Number of Pages Required

5+ page

Colors
0054AA
0677BA
7BADD7
CADEEF
E8F1F8
FFC000
F8CF3A
FAE287
FDF2CF
FEFAEE
EE7325
F08F49
F5BC92
FAE3D3
FDF4ED

Requirements
Must have
• Clean, colorful, and professional

```html
<!DOCTYPE html>
<html lang="en">
<head>
<meta charset="UTF-8">
<title>Tidewell Heating — Water Heater Services</title>
<link href="https://fonts.googleapis.com/css2?family=Lexend:wght@500;600;700&family=Inter:ital,wght@0,400;0,500;0,600;0,700;1,400&display=swap" rel="stylesheet">
<style>
:root{
  --blue:#0054AA;--blue2:#0677BA;--blue3:#7BADD7;--blue4:#CADEEF;--blue5:#E8F1F8;
  --yellow:#FFC000;--yellow2:#F8CF3A;--yellow3:#FAE287;--yellow4:#FDF2CF;--yellow5:#FEFAEE;
  --orange:#EE7325;--orange2:#F08F49;--orange3:#F5BC92;--orange4:#FAE3D3;--orange5:#FDF4ED;
  --ink:#14213a;--text:#4a5568;--muted:#6b7280;--line:#e3e8ef;--footer:#1b2233;
}
*{box-sizing:border-box;margin:0;padding:0}
html,body{width:1200px;height:3333px;overflow:hidden}
body{font-family:'Inter',sans-serif;color:var(--ink);background:#fff}
h1,h2,h3,.display{font-family:'Lexend',sans-serif}
.wrap{width:570px;margin-left:315px;position:relative}
svg.ic{width:14px;height:14px;fill:none;stroke:currentColor;stroke-width:2;stroke-linecap:round;stroke-linejoin:round;flex:none}

.topbar{height:18px;background:var(--blue);border-bottom:2px solid var(--yellow);color:#fff;font-size:7px}
.topbar .wrap{display:flex;justify-content:space-between;align-items:center;height:16px}
.topbar span{display:inline-flex;align-items:center;gap:3px;margin-right:10px}
.topbar svg.ic{width:8px;height:8px}

.header{height:78px;box-shadow:0 2px 6px rgba(0,0,0,.06);position:relative;z-index:2}
.header .row{display:flex;justify-content:space-between;align-items:center;height:54px}
.brand{display:flex;align-items:center;gap:6px;font-family:'Lexend',sans-serif;font-weight:700;color:var(--blue);font-size:13px}
.brand i{width:18px;height:18px;border-radius:50%;background:var(--yellow)}
.hbtns{display:flex;gap:8px}
.btn{display:inline-flex;align-items:center;gap:6px;font-weight:600;font-size:9px;border-radius:4px;color:#fff;padding:0 14px;height:27px}
.btn-blue{background:var(--blue)}
.btn-orange{background:var(--orange)}
.btn svg.ic{width:10px;height:10px}
.nav{display:flex;justify-content:center;gap:16px;font-size:8px;color:#333;border-top:1px solid #eef1f5;height:24px;align-items:center;margin:0 -2px}
.nav a{padding:4px 7px;border-radius:3px}
.nav .active{background:var(--yellow);font-weight:600}

.hero{height:379px;background:linear-gradient(90deg,#fff 60%,#f7f9fc)}
.hero .wrap{height:379px}
.pill{display:inline-block;font-size:6.5px;font-weight:700;border-radius:10px;padding:4px 8px}
.hero .pill{position:absolute;top:46px;background:var(--orange);color:#fff;box-shadow:0 0 0 2px var(--yellow) inset}
.hero h1{position:absolute;top:70px;width:280px;font-size:29px;line-height:33px;font-weight:700;letter-spacing:-.5px}
.hero p.lead{position:absolute;top:184px;width:265px;font-size:10px;line-height:15px;color:var(--text)}
.hero .cta{position:absolute;top:244px;display:flex;gap:8px}
.hero .cta .btn{height:29px;padding:0 16px}
.stats{position:absolute;top:292px;display:flex;gap:7px}
.stat{width:87px;height:41px;border-radius:5px;text-align:center;padding-top:8px}
.stat b{display:block;font-family:'Lexend',sans-serif;font-size:15px;line-height:15px}
.stat small{font-size:5.5px;color:var(--text)}
.s1{background:var(--blue5)}.s1 b{color:var(--blue)}
.s2{background:var(--yellow5)}.s2 b{color:var(--orange)}
.s3{background:var(--orange5)}.s3 b{color:var(--blue)}
.hero-photo{position:absolute;left:296px;top:98px;width:274px;height:182px;border-radius:6px;border:2px solid var(--yellow);background:linear-gradient(135deg,#6b7684,#3a4454 55%,#1f2c44);box-shadow:0 10px 24px rgba(0,0,0,.18);overflow:hidden}
.hero-photo span{position:absolute;left:12px;bottom:12px;color:#fff;font-size:9px;font-weight:600}

.strip{height:115px;background:#f5f7fa;border-top:2px solid var(--blue);border-bottom:2px solid var(--blue)}
.strip .wrap{display:flex;gap:8px;padding-top:17px}
.fcard{width:88px;height:76px;background:#fff;border-left:3px solid var(--orange);border-radius:4px;box-shadow:0 2px 6px rgba(0,0,0,.07);text-align:center;padding-top:9px}
.ocirc{width:20px;height:20px;border-radius:50%;background:var(--orange2);color:#fff;display:inline-flex;align-items:center;justify-content:center}
.ocirc svg.ic{width:11px;height:11px}
.fcard h4{font-size:10px;line-height:11px;font-weight:700;margin-top:5px}
.fcard small{display:block;font-size:5px;color:var(--muted);margin-top:2px}

.shead{text-align:center}
.shead .pill{background:var(--blue5);color:var(--blue)}
.shead h2{font-size:20px;font-weight:700;margin-top:12px;letter-spacing:-.3px}
.shead p{font-size:9px;color:var(--text);margin:8px auto 0;width:320px;line-height:14px}

.services{height:411px;padding-top:49px}
.sgrid{display:grid;grid-template-columns:repeat(3,182px);gap:12px 12px;margin-top:30px}
.scard{border:1px solid var(--line);border-radius:6px;padding:12px;background:#fff;box-shadow:0 1px 3px rgba(0,0,0,.04)}
.scard.tall{height:104px}.scard.short{height:100px}
.scard .top{display:flex;gap:9px;align-items:flex-start}
.bsq{width:28px;height:28px;border-radius:6px;background:var(--blue);color:#fff;display:flex;align-items:center;justify-content:center;flex:none}
.bsq svg.ic{width:13px;height:13px}
.scard h3{font-family:'Inter',sans-serif;font-size:9.5px;font-weight:700;line-height:12px;letter-spacing:-.1px}
.scard p{font-size:7.5px;line-height:12px;color:var(--text);margin-top:6px}
.more{display:inline-flex;align-items:center;gap:3px;color:var(--orange);font-size:7px;font-weight:600;margin-top:7px}
.more svg.ic{width:7px;height:7px}

.why{height:321px;background:linear-gradient(180deg,var(--blue),var(--blue2));padding-top:48px;color:#fff}
.why .pill{background:rgba(255,255,255,.2);color:#fff}
.why h2{color:#fff}
.why .shead p{color:#e6eef8}
.wgrid{display:grid;grid-template-columns:repeat(3,183px);gap:11px 11px;margin-top:25px}
.wcard{background:#fff;border:2px solid var(--yellow3);border-radius:5px;padding:10px;display:flex;gap:8px;color:var(--ink)}
.wgrid .r1{height:70px}.wgrid .r2{height:60px}
.ysq{width:22px;height:22px;border-radius:5px;background:var(--orange2);color:#fff;display:flex;align-items:center;justify-content:center;flex:none}
.ysq svg.ic{width:11px;height:11px}
.wcard h4{font-size:10px;line-height:11px;font-weight:700}
.wcard small{display:block;font-size:6.5px;color:var(--muted);margin-top:5px;line-height:9px}

.warr{height:362px;padding-top:46px}
.wbox{width:510px;height:272px;margin-left:345px;border-radius:6px;border:2px solid var(--yellow);background:linear-gradient(135deg,var(--orange),var(--orange2));box-shadow:0 10px 24px rgba(238,115,37,.25);text-align:center;color:#fff;padding-top:21px}
.wbox h2{font-size:20px;font-weight:700;letter-spacing:-.3px}
.wbox p{font-size:9px;margin-top:7px;color:#fff5ec}
.wpair{display:flex;gap:14px;justify-content:center;margin-top:15px}
.wcardlg{width:223px;height:110px;background:#fff;border:3px solid var(--yellow);border-radius:5px;color:var(--ink);padding-top:14px}
.bigc{width:38px;height:38px;border-radius:50%;display:inline-flex;align-items:center;justify-content:center;color:#fff}
.bigc svg.ic{width:18px;height:18px}
.wcardlg h3{font-size:14px;font-weight:600;margin-top:8px}
.wcardlg small{font-size:7px;color:var(--text)}
.wbar{width:462px;height:34px;margin:16px auto 0;background:rgba(255,255,255,.18);border-radius:5px;display:flex;justify-content:center;align-items:center;gap:12px;font-size:7px;font-weight:500}
.wbar span{display:inline-flex;align-items:center;gap:4px}
.wbar svg.ic{width:8px;height:8px}

.tests{height:357px;background:#f5f7fa;padding-top:49px}
.tests .pill{background:var(--yellow);color:#fff}
.tgrid{display:grid;grid-template-columns:repeat(3,183px);gap:11px 11px;margin-top:26px}
.tcard{height:83px;border-top:3px solid var(--yellow);border-radius:5px;background:linear-gradient(135deg,#fff,var(--blue5));box-shadow:0 2px 6px rgba(0,0,0,.06);padding:9px 11px}
.stars{display:flex;gap:3px}
.stars svg{width:8px;height:8px;fill:var(--yellow)}
.tcard q{display:block;font-style:italic;font-size:7px;line-height:12px;color:var(--text);margin-top:8px;height:26px;quotes:'"' '"'}
.loc{display:flex;align-items:center;gap:3px;font-size:6.5px;color:#333;margin-top:7px}
.loc svg.ic{width:7px;height:7px;color:var(--blue)}

.area{height:393px;padding-top:47px}
.area .row{position:relative;height:230px;margin-top:32px}
.cities{position:absolute;left:0;top:40px;width:277px;height:128px;border:2px solid var(--blue);border-radius:6px;background:linear-gradient(135deg,#fff,var(--blue5));padding:14px 16px}
.cities h3{font-size:14px;font-weight:600}
.clist{display:grid;grid-template-columns:1fr 1fr;gap:6px 0;margin-top:10px;font-size:6.5px}
.clist span{display:flex;align-items:center;gap:4px}
.clist svg.ic{width:7px;height:7px;color:var(--orange)}
.map{position:absolute;left:293px;top:0;width:277px;height:209px;border:2px solid var(--yellow);border-radius:6px;background:linear-gradient(135deg,#fbfcfe,#f2f6fb);box-shadow:0 4px 12px rgba(0,0,0,.06)}

.quote{height:563px;padding-top:45px;background:#fff}
.qform{width:388px;height:470px;margin-left:406px;background:linear-gradient(180deg,var(--blue),var(--blue2));border:2px solid var(--yellow);border-radius:6px;padding:20px 20px;color:#fff;box-shadow:0 10px 24px rgba(0,84,170,.25)}
.qform h2{text-align:center;font-size:20px;font-weight:700}
.qform .sub{text-align:center;font-size:8.5px;margin-top:6px;color:#e6eef8}
.qgrid{display:grid;grid-template-columns:1fr 1fr;gap:0 14px;margin-top:16px}
.field{margin-bottom:12px}
.field label{display:block;font-size:7.5px;font-weight:600;margin-bottom:5px}
.field .in{height:25px;border-radius:4px;background:rgba(255,255,255,.04);font-size:7px;color:rgba(255,255,255,.35);padding:8px 8px}
.field .sel{height:23px;background:#fff;color:#333;border-radius:3px;font-size:7.5px;padding:0 10px;display:flex;align-items:center;justify-content:space-between}
.field .ta{height:78px}
.full{grid-column:1/3}
.submit{height:29px;background:var(--orange);border-radius:4px;display:flex;align-items:center;justify-content:center;gap:6px;font-size:8.5px;font-weight:700;margin-top:2px}
.submit svg.ic{width:9px;height:9px}
.consent{margin-top:9px;height:34px;background:rgba(255,255,255,.15);border-radius:4px;display:flex;gap:6px;padding:8px 10px;font-size:6.3px;line-height:10px}
.consent svg.ic{width:8px;height:8px;color:var(--yellow)}

.mission{height:141px;background:linear-gradient(180deg,var(--blue),#0a5ba8);border-top:3px solid var(--yellow);border-bottom:3px solid var(--yellow);text-align:center;color:#fff;padding-top:37px}
.mission h2{font-size:20px;font-weight:700}
.mission p{width:400px;margin:12px auto 0;font-size:9px;line-height:15px;color:#e6eef8}

.footer{height:192px;background:var(--footer);color:#c7ccd6;padding-top:32px}
.fcols{display:grid;grid-template-columns:146px 146px 146px 132px;height:118px}
.fcols h5{font-family:'Lexend',sans-serif;color:var(--yellow);font-size:10px;font-weight:600;margin-bottom:8px}
.fcols li{list-style:none;font-size:7.5px;margin-bottom:8px;display:flex;align-items:center;gap:6px}
.fcols li svg.ic{width:9px;height:9px;color:#fff}
.fbrand{display:flex;align-items:center;gap:5px;font-family:'Lexend',sans-serif;font-weight:700;color:#fff;font-size:11px;height:28px}
.fbrand i{width:14px;height:14px;background:var(--yellow);border-radius:2px}
.fabout{font-size:7px;line-height:11.5px;margin-top:6px;width:125px}
.social{display:flex;gap:6px;margin-top:9px}
.social i{width:15px;height:15px;border-radius:3px;background:var(--blue2)}
.fbottom{border-top:1px solid #2e374b;display:flex;justify-content:space-between;font-size:6.5px;padding-top:14px;color:#9aa2b2}
</style>
</head>
<body>

<div class="topbar"><div class="wrap">
  <div><span><svg class="ic" viewBox="0 0 24 24"><path d="M5 4h4l2 5-2.5 1.5a11 11 0 0 0 5 5L15 13l5 2v4a2 2 0 0 1-2 2A16 16 0 0 1 3 6a2 2 0 0 1 2-2"/></svg>(555) 555-5555</span><span><svg class="ic" viewBox="0 0 24 24"><rect x="3" y="5" width="18" height="14" rx="2"/><path d="m3 7 9 6 9-6"/></svg>info@tidewellheating.com</span></div>
  <span style="margin:0"><svg class="ic" viewBox="0 0 24 24"><path d="M12 21s-7-6-7-11a7 7 0 0 1 14 0c0 5-7 11-7 11z"/><circle cx="12" cy="10" r="2.5"/></svg>Serving All Palm Beach County, FL</span>
</div></div>

<header class="header"><div class="wrap">
  <div class="row">
    <div class="brand"><i></i>Tidewell Heating</div>
    <div class="hbtns">
      <span class="btn btn-blue"><svg class="ic" viewBox="0 0 24 24"><path d="M5 4h4l2 5-2.5 1.5a11 11 0 0 0 5 5L15 13l5 2v4a2 2 0 0 1-2 2A16 16 0 0 1 3 6a2 2 0 0 1 2-2"/></svg>Call Now</span>
      <span class="btn btn-orange">Get Free Quote <svg class="ic" viewBox="0 0 24 24"><path d="m9 6 6 6-6 6"/></svg></span>
    </div>
  </div>
  <nav class="nav"><a class="active">Home</a><a>Gas Water Heaters</a><a>Electric Water Heaters</a><a>Tankless Water Heaters</a><a>About Us</a><a>Contact</a></nav>
</div></header>

<section class="hero"><div class="wrap">
  <span class="pill">#1 Water Heater Specialists in Palm Beach County</span>
  <h1>Fast &amp; Reliable Water Heater Services</h1>
  <p class="lead">Same-day installation, repair, and replacement for gas, electric, and tankless water heaters — backed by industry-leading warranties.</p>
  <div class="cta">
    <span class="btn btn-blue"><svg class="ic" viewBox="0 0 24 24"><path d="M5 4h4l2 5-2.5 1.5a11 11 0 0 0 5 5L15 13l5 2v4a2 2 0 0 1-2 2A16 16 0 0 1 3 6a2 2 0 0 1 2-2"/></svg>(555) 555-5555</span>
    <span class="btn btn-orange">Get Free Quote <svg class="ic" viewBox="0 0 24 24"><path d="M5 12h14M13 6l6 6-6 6"/></svg></span>
  </div>
  <div class="stats">
    <div class="stat s1"><b>15</b><small>Year Warranty</small></div>
    <div class="stat s2"><b>100%</b><small>Satisfaction</small></div>
    <div class="stat s3"><b>24/7</b><small>Emergency</small></div>
  </div>
  <div class="hero-photo" role="img" aria-label="Photo of a technician standing beside tank and tankless water heaters in a warehouse"><span>Licensed &amp; Insured Professionals</span></div>
</div></section>

<section class="strip"><div class="wrap">
  <div class="fcard"><span class="ocirc"><svg class="ic" viewBox="0 0 24 24"><circle cx="12" cy="12" r="9"/><path d="M12 7v5l3 2"/></svg></span><h4>Same-Day<br>Service</h4></div>
  <div class="fcard"><span class="ocirc"><svg class="ic" viewBox="0 0 24 24"><path d="M12 3v18M16 7H10a3 3 0 0 0 0 6h4a3 3 0 0 1 0 6H7"/></svg></span><h4>Best Price<br>Guarantee</h4></div>
  <div class="fcard"><span class="ocirc"><svg class="ic" viewBox="0 0 24 24"><path d="m12 3 2.7 5.6 6.1.9-4.4 4.3 1 6.1L12 17l-5.4 2.9 1-6.1-4.4-4.3 6.1-.9z"/></svg></span><h4>100%<br>Satisfaction</h4></div>
  <div class="fcard"><span class="ocirc"><svg class="ic" viewBox="0 0 24 24"><path d="M12 3 5 6v6c0 4.5 3 8 7 9 4-1 7-4.5 7-9V6z"/></svg></span><h4>15-Year<br>Warranty</h4><small>Heater &amp; Parts</small></div>
  <div class="fcard"><span class="ocirc"><svg class="ic" viewBox="0 0 24 24"><circle cx="12" cy="9" r="5"/><path d="m9 13-2 8 5-3 5 3-2-8"/></svg></span><h4>Lifetime<br>Warranty</h4><small>Workmanship</small></div>
  <div class="fcard"><span class="ocirc"><svg class="ic" viewBox="0 0 24 24"><circle cx="12" cy="12" r="9"/><path d="m8 12 3 3 5-6"/></svg></span><h4>Transferable</h4><small>All Warranties</small></div>
</div></section>

<section class="services"><div class="wrap">
  <div class="shead"><span class="pill">WHAT WE DO</span><h2>Complete Water Heater Solutions</h2><p>Professional installation, repair, and replacement services for all water heater types</p></div>
  <div class="sgrid">
    <div class="scard tall"><div class="top"><span class="bsq"><svg class="ic" viewBox="0 0 24 24"><path d="M14 6a4 4 0 0 0 5 5l-9 9a2 2 0 0 1-3-3l9-9a4 4 0 0 0-2-2z"/></svg></span><h3 style="white-space:nowrap">Water Heater Installation</h3></div><p>Professional installation of gas, electric, and tankless water heaters with full code compliance and warranty protection.</p></div>
    <div class="scard tall"><div class="top"><span class="bsq"><svg class="ic" viewBox="0 0 24 24"><path d="M13 2 4 14h7l-1 8 9-12h-7z"/></svg></span><h3>Water Heater Repair</h3></div><p>Fast diagnosis and repair for leaks, no-hot-water issues, pilot light failures, and electrical or thermostat problems.</p></div>
    <div class="scard tall"><div class="top"><span class="bsq"><svg class="ic" viewBox="0 0 24 24"><path d="M7 10v11H4V10zM7 10l4-7a2 2 0 0 1 3 2l-1 4h6a2 2 0 0 1 2 2l-2 8a2 2 0 0 1-2 2H7"/></svg></span><h3>Water Heater<br>Replacement</h3></div><p>Upgrade your failing water heater with a high-efficiency model designed for reliability and performance.</p></div>
    <div class="scard short"><div class="top"><span class="bsq"><svg class="ic" viewBox="0 0 24 24"><path d="M12 3c3 4 5 6 5 10a5 5 0 0 1-10 0c0-2 1-3 2-4 0 2 1 3 2 3 0-3-1-6 1-9z"/></svg></span><h3>Gas Water Heaters</h3></div><p>Powerful, cost-effective hot water systems for homes and businesses.</p><span class="more">Learn More <svg class="ic" viewBox="0 0 24 24"><path d="M5 12h14M13 6l6 6-6 6"/></svg></span></div>
    <div class="scard short"><div class="top"><span class="bsq"><svg class="ic" viewBox="0 0 24 24"><rect x="3" y="7" width="15" height="10" rx="2"/><path d="M21 10v4"/></svg></span><h3>Electric Water Heaters</h3></div><p>Safe, efficient electric water heating solutions for modern properties.</p><span class="more">Learn More <svg class="ic" viewBox="0 0 24 24"><path d="M5 12h14M13 6l6 6-6 6"/></svg></span></div>
    <div class="scard short"><div class="top"><span class="bsq"><svg class="ic" viewBox="0 0 24 24"><path d="M12 3s6 7 6 11a6 6 0 0 1-12 0c0-4 6-11 6-11z"/></svg></span><h3>Tankless Water Heaters</h3></div><p>On-demand hot water with endless supply and energy savings.</p><span class="more">Learn More <svg class="ic" viewBox="0 0 24 24"><path d="M5 12h14M13 6l6 6-6 6"/></svg></span></div>
  </div>
</div></section>

<section class="why"><div class="wrap">
  <div class="shead"><span class="pill">WHY CHOOSE US</span><h2>Water Heater Specialists You Can Trust</h2><p style="width:400px">Unlike general plumbers, we specialize exclusively in water heaters</p></div>
  <div class="wgrid">
    <div class="wcard r1"><span class="ysq"><svg class="ic" viewBox="0 0 24 24"><circle cx="12" cy="12" r="9"/><path d="M12 7v5l3 2"/></svg></span><div><h4>Same-Day Service Available</h4><small>Emergency response when you need it most</small></div></div>
    <div class="wcard r1"><span class="ysq"><svg class="ic" viewBox="0 0 24 24"><path d="M12 3v18M16 7H10a3 3 0 0 0 0 6h4a3 3 0 0 1 0 6H7"/></svg></span><div><h4>Upfront Transparent Pricing</h4><small>No hidden fees or surprise charges</small></div></div>
    <div class="wcard r1"><span class="ysq"><svg class="ic" viewBox="0 0 24 24"><path d="M12 3v18M16 7H10a3 3 0 0 0 0 6h4a3 3 0 0 1 0 6H7"/></svg></span><div><h4>Best Price Guarantee</h4><small>We match or beat competitor quotes</small></div></div>
    <div class="wcard r2"><span class="ysq"><svg class="ic" viewBox="0 0 24 24"><circle cx="12" cy="9" r="5"/><path d="m9 13-2 8 5-3 5 3-2-8"/></svg></span><div><h4>Licensed &amp; Insured Technicians</h4><small>Fully trained and certified experts</small></div></div>
    <div class="wcard r2"><span class="ysq"><svg class="ic" viewBox="0 0 24 24"><path d="m12 3 2.7 5.6 6.1.9-4.4 4.3 1 6.1L12 17l-5.4 2.9 1-6.1-4.4-4.3 6.1-.9z"/></svg></span><div><h4>100% Satisfaction Rating</h4><small>Thousands of happy customers</small></div></div>
    <div class="wcard r2"><span class="ysq"><svg class="ic" viewBox="0 0 24 24"><circle cx="12" cy="12" r="9"/><path d="m8 12 3 3 5-6"/></svg></span><div><h4>Transferable Warranties</h4><small>Protection for homeowners and buyers</small></div></div>
  </div>
</div></section>

<section class="warr">
  <div class="wbox">
    <h2>Industry-Leading Warranties</h2>
    <p>Every installation and replacement is backed by unbeatable protection</p>
    <div class="wpair">
      <div class="wcardlg"><span class="bigc" style="background:var(--blue)"><svg class="ic" viewBox="0 0 24 24"><path d="M12 3 5 6v6c0 4.5 3 8 7 9 4-1 7-4.5 7-9V6z"/></svg></span><h3>15-Year Warranty</h3><small>On Water Heater &amp; Parts</small></div>
      <div class="wcardlg"><span class="bigc" style="background:var(--orange)"><svg class="ic" viewBox="0 0 24 24"><circle cx="12" cy="9" r="5"/><path d="m9 13-2 8 5-3 5 3-2-8"/></svg></span><h3>Lifetime Warranty</h3><small>On Workmanship</small></div>
    </div>
    <div class="wbar">
      <span><svg class="ic" viewBox="0 0 24 24"><circle cx="12" cy="12" r="9"/><path d="m8 12 3 3 5-6"/></svg>100% Satisfaction Guarantee</span>
      <span><svg class="ic" viewBox="0 0 24 24"><circle cx="12" cy="12" r="9"/><path d="m8 12 3 3 5-6"/></svg>Best Price Guarantee</span>
      <span><svg class="ic" viewBox="0 0 24 24"><circle cx="12" cy="12" r="9"/><path d="m8 12 3 3 5-6"/></svg>Warranties Transfer Upon Home Sale</span>
    </div>
  </div>
</section>

<section class="tests"><div class="wrap">
  <div class="shead"><span class="pill">TESTIMONIALS</span><h2>What Our Customers Say</h2><p>Trusted by thousands of homeowners across Palm Beach County</p></div>
  <div class="tgrid">
    <div class="tcard"><div class="stars"><svg viewBox="0 0 24 24"><path d="m12 2 3 6.5 7 .8-5.2 4.8 1.4 7L12 17.6 5.8 21.1l1.4-7L2 9.3l7-.8z"/></svg><svg viewBox="0 0 24 24"><path d="m12 2 3 6.5 7 .8-5.2 4.8 1.4 7L12 17.6 5.8 21.1l1.4-7L2 9.3l7-.8z"/></svg><svg viewBox="0 0 24 24"><path d="m12 2 3 6.5 7 .8-5.2 4.8 1.4 7L12 17.6 5.8 21.1l1.4-7L2 9.3l7-.8z"/></svg><svg viewBox="0 0 24 24"><path d="m12 2 3 6.5 7 .8-5.2 4.8 1.4 7L12 17.6 5.8 21.1l1.4-7L2 9.3l7-.8z"/></svg><svg viewBox="0 0 24 24"><path d="m12 2 3 6.5 7 .8-5.2 4.8 1.4 7L12 17.6 5.8 21.1l1.4-7L2 9.3l7-.8z"/></svg></div><q>Fast, professional, and affordable. My water heater was replaced the same day I called.</q><div class="loc"><svg class="ic" viewBox="0 0 24 24"><path d="M12 21s-7-6-7-11a7 7 0 0 1 14 0c0 5-7 11-7 11z"/></svg>Palm Beach Gardens</div></div>
    <div class="tcard"><div class="stars"><svg viewBox="0 0 24 24"><path d="m12 2 3 6.5 7 .8-5.2 4.8 1.4 7L12 17.6 5.8 21.1l1.4-7L2 9.3l7-.8z"/></svg><svg viewBox="0 0 24 24"><path d="m12 2 3 6.5 7 .8-5.2 4.8 1.4 7L12 17.6 5.8 21.1l1.4-7L2 9.3l7-.8z"/></svg><svg viewBox="0 0 24 24"><path d="m12 2 3 6.5 7 .8-5.2 4.8 1.4 7L12 17.6 5.8 21.1l1.4-7L2 9.3l7-.8z"/></svg><svg viewBox="0 0 24 24"><path d="m12 2 3 6.5 7 .8-5.2 4.8 1.4 7L12 17.6 5.8 21.1l1.4-7L2 9.3l7-.8z"/></svg><svg viewBox="0 0 24 24"><path d="m12 2 3 6.5 7 .8-5.2 4.8 1.4 7L12 17.6 5.8 21.1l1.4-7L2 9.3l7-.8z"/></svg></div><q>They explained everything clearly and the warranty coverage is incredible.</q><div class="loc"><svg class="ic" viewBox="0 0 24 24"><path d="M12 21s-7-6-7-11a7 7 0 0 1 14 0c0 5-7 11-7 11z"/></svg>Boca Raton</div></div>
    <div class="tcard"><div class="stars"><svg viewBox="0 0 24 24"><path d="m12 2 3 6.5 7 .8-5.2 4.8 1.4 7L12 17.6 5.8 21.1l1.4-7L2 9.3l7-.8z"/></svg><svg viewBox="0 0 24 24"><path d="m12 2 3 6.5 7 .8-5.2 4.8 1.4 7L12 17.6 5.8 21.1l1.4-7L2 9.3l7-.8z"/></svg><svg viewBox="0 0 24 24"><path d="m12 2 3 6.5 7 .8-5.2 4.8 1.4 7L12 17.6 5.8 21.1l1.4-7L2 9.3l7-.8z"/></svg><svg viewBox="0 0 24 24"><path d="m12 2 3 6.5 7 .8-5.2 4.8 1.4 7L12 17.6 5.8 21.1l1.4-7L2 9.3l7-.8z"/></svg><svg viewBox="0 0 24 24"><path d="m12 2 3 6.5 7 .8-5.2 4.8 1.4 7L12 17.6 5.8 21.1l1.4-7L2 9.3l7-.8z"/></svg></div><q>Best experience I've had with a home service company. Highly recommend!</q><div class="loc"><svg class="ic" viewBox="0 0 24 24"><path d="M12 21s-7-6-7-11a7 7 0 0 1 14 0c0 5-7 11-7 11z"/></svg>West Palm Beach</div></div>
    <div class="tcard"><div class="stars"><svg viewBox="0 0 24 24"><path d="m12 2 3 6.5 7 .8-5.2 4.8 1.4 7L12 17.6 5.8 21.1l1.4-7L2 9.3l7-.8z"/></svg><svg viewBox="0 0 24 24"><path d="m12 2 3 6.5 7 .8-5.2 4.8 1.4 7L12 17.6 5.8 21.1l1.4-7L2 9.3l7-.8z"/></svg><svg viewBox="0 0 24 24"><path d="m12 2 3 6.5 7 .8-5.2 4.8 1.4 7L12 17.6 5.8 21.1l1.4-7L2 9.3l7-.8z"/></svg><svg viewBox="0 0 24 24"><path d="m12 2 3 6.5 7 .8-5.2 4.8 1.4 7L12 17.6 5.8 21.1l1.4-7L2 9.3l7-.8z"/></svg><svg viewBox="0 0 24 24"><path d="m12 2 3 6.5 7 .8-5.2 4.8 1.4 7L12 17.6 5.8 21.1l1.4-7L2 9.3l7-.8z"/></svg></div><q>The technician was knowledgeable, clean, and completed the job perfectly.</q><div class="loc"><svg class="ic" viewBox="0 0 24 24"><path d="M12 21s-7-6-7-11a7 7 0 0 1 14 0c0 5-7 11-7 11z"/></svg>Delray Beach</div></div>
    <div class="tcard"><div class="stars"><svg viewBox="0 0 24 24"><path d="m12 2 3 6.5 7 .8-5.2 4.8 1.4 7L12 17.6 5.8 21.1l1.4-7L2 9.3l7-.8z"/></svg><svg viewBox="0 0 24 24"><path d="m12 2 3 6.5 7 .8-5.2 4.8 1.4 7L12 17.6 5.8 21.1l1.4-7L2 9.3l7-.8z"/></svg><svg viewBox="0 0 24 24"><path d="m12 2 3 6.5 7 .8-5.2 4.8 1.4 7L12 17.6 5.8 21.1l1.4-7L2 9.3l7-.8z"/></svg><svg viewBox="0 0 24 24"><path d="m12 2 3 6.5 7 .8-5.2 4.8 1.4 7L12 17.6 5.8 21.1l1.4-7L2 9.3l7-.8z"/></svg><svg viewBox="0 0 24 24"><path d="m12 2 3 6.5 7 .8-5.2 4.8 1.4 7L12 17.6 5.8 21.1l1.4-7L2 9.3l7-.8z"/></svg></div><q>Great pricing and the lifetime warranty on workmanship sealed the deal.</q><div class="loc"><svg class="ic" viewBox="0 0 24 24"><path d="M12 21s-7-6-7-11a7 7 0 0 1 14 0c0 5-7 11-7 11z"/></svg>Boynton Beach</div></div>
    <div class="tcard"><div class="stars"><svg viewBox="0 0 24 24"><path d="m12 2 3 6.5 7 .8-5.2 4.8 1.4 7L12 17.6 5.8 21.1l1.4-7L2 9.3l7-.8z"/></svg><svg viewBox="0 0 24 24"><path d="m12 2 3 6.5 7 .8-5.2 4.8 1.4 7L12 17.6 5.8 21.1l1.4-7L2 9.3l7-.8z"/></svg><svg viewBox="0 0 24 24"><path d="m12 2 3 6.5 7 .8-5.2 4.8 1.4 7L12 17.6 5.8 21.1l1.4-7L2 9.3l7-.8z"/></svg><svg viewBox="0 0 24 24"><path d="m12 2 3 6.5 7 .8-5.2 4.8 1.4 7L12 17.6 5.8 21.1l1.4-7L2 9.3l7-.8z"/></svg><svg viewBox="0 0 24 24"><path d="m12 2 3 6.5 7 .8-5.2 4.8 1.4 7L12 17.6 5.8 21.1l1.4-7L2 9.3l7-.8z"/></svg></div><q>Called them for an emergency repair and they arrived within 2 hours. Amazing service!</q><div class="loc"><svg class="ic" viewBox="0 0 24 24"><path d="M12 21s-7-6-7-11a7 7 0 0 1 14 0c0 5-7 11-7 11z"/></svg>Jupiter</div></div>
  </div>
</div></section>

<section class="area"><div class="wrap">
  <div class="shead"><span class="pill">SERVICE AREA</span><h2>Proudly Serving Palm Beach County</h2><p style="width:400px">Fast, reliable water heater service throughout Florida's Palm Beach County</p></div>
  <div class="row">
    <div class="cities">
      <h3>Cities We Serve</h3>
      <div class="clist">
        <span><svg class="ic" viewBox="0 0 24 24"><path d="M12 21s-7-6-7-11a7 7 0 0 1 14 0c0 5-7 11-7 11z"/></svg>West Palm Beach</span>
        <span><svg class="ic" viewBox="0 0 24 24"><path d="M12 21s-7-6-7-11a7 7 0 0 1 14 0c0 5-7 11-7 11z"/></svg>Boca Raton</span>
        <span><svg class="ic" viewBox="0 0 24 24"><path d="M12 21s-7-6-7-11a7 7 0 0 1 14 0c0 5-7 11-7 11z"/></svg>Delray Beach</span>
        <span><svg class="ic" viewBox="0 0 24 24"><path d="M12 21s-7-6-7-11a7 7 0 0 1 14 0c0 5-7 11-7 11z"/></svg>Boynton Beach</span>
        <span><svg class="ic" viewBox="0 0 24 24"><path d="M12 21s-7-6-7-11a7 7 0 0 1 14 0c0 5-7 11-7 11z"/></svg>Palm Beach Gardens</span>
        <span><svg class="ic" viewBox="0 0 24 24"><path d="M12 21s-7-6-7-11a7 7 0 0 1 14 0c0 5-7 11-7 11z"/></svg>Jupiter</span>
        <span><svg class="ic" viewBox="0 0 24 24"><path d="M12 21s-7-6-7-11a7 7 0 0 1 14 0c0 5-7 11-7 11z"/></svg>Lake Worth</span>
        <span><svg class="ic" viewBox="0 0 24 24"><path d="M12 21s-7-6-7-11a7 7 0 0 1 14 0c0 5-7 11-7 11z"/></svg>Wellington</span>
        <span><svg class="ic" viewBox="0 0 24 24"><path d="M12 21s-7-6-7-11a7 7 0 0 1 14 0c0 5-7 11-7 11z"/></svg>Royal Palm Beach</span>
        <span><svg class="ic" viewBox="0 0 24 24"><path d="M12 21s-7-6-7-11a7 7 0 0 1 14 0c0 5-7 11-7 11z"/></svg>Greenacres</span>
      </div>
    </div>
    <div class="map" role="img" aria-label="Map of Palm Beach County, Florida service area"></div>
  </div>
</div></section>

<section class="quote">
  <div class="qform">
    <h2>Get Your Free Quote</h2>
    <p class="sub">Fill out the form below and we'll get back to you within 24 hours</p>
    <div class="qgrid">
      <div class="field"><label>Full Name *</label><div class="in">John Smith</div></div>
      <div class="field"><label>Phone Number *</label><div class="in">(555) 555-5555</div></div>
      <div class="field full"><label>Email Address *</label><div class="in">you@example.com</div></div>
      <div class="field full"><label>Service Address *</label><div class="in">123 Main St, West Palm Beach, FL</div></div>
      <div class="field full"><label>Service Needed *</label><div class="sel">Select a service... <svg class="ic" style="width:8px;height:8px" viewBox="0 0 24 24"><path d="m6 9 6 6 6-6"/></svg></div></div>
      <div class="field full"><label>Additional Details</label><div class="in ta">Tell us more about your needs...</div></div>
    </div>
    <div class="submit"><svg class="ic" viewBox="0 0 24 24"><path d="M22 2 11 13M22 2l-7 20-4-9-9-4z"/></svg>Submit Request</div>
    <div class="consent"><svg class="ic" viewBox="0 0 24 24"><circle cx="12" cy="12" r="9"/><path d="m8 12 3 3 5-6"/></svg><span>By submitting this form, you agree to be contacted by Tidewell Heating regarding your service request. We respect your privacy and will never share your information.</span></div>
  </div>
</section>

<section class="mission">
  <h2>Our Mission</h2>
  <p>Our mission is to provide fast, honest, and reliable water heater service while delivering unmatched value, long-term protection, and complete customer satisfaction.</p>
</section>

<footer class="footer"><div class="wrap">
  <div class="fcols">
    <div>
      <div class="fbrand"><i></i>Tidewell Heating</div>
      <p class="fabout">Palm Beach County's trusted water heater experts. Fast, reliable service backed by industry-leading warranties.</p>
      <div class="social"><i></i><i></i><i></i></div>
    </div>
    <div><h5>Quick Links</h5><ul><li>Home</li><li>About Us</li><li>Contact Us</li><li>Privacy Policy</li></ul></div>
    <div><h5>Our Services</h5><ul><li>Gas Water Heaters</li><li>Electric Water Heaters</li><li>Tankless Water Heaters</li></ul></div>
    <div><h5>Contact Us</h5><ul>
      <li><svg class="ic" viewBox="0 0 24 24"><path d="M5 4h4l2 5-2.5 1.5a11 11 0 0 0 5 5L15 13l5 2v4a2 2 0 0 1-2 2A16 16 0 0 1 3 6a2 2 0 0 1 2-2"/></svg>(555) 555-5555</li>
      <li><svg class="ic" viewBox="0 0 24 24"><rect x="3" y="5" width="18" height="14" rx="2"/><path d="m3 7 9 6 9-6"/></svg>info@tidewellheating.com</li>
      <li><svg class="ic" viewBox="0 0 24 24"><path d="M12 21s-7-6-7-11a7 7 0 0 1 14 0c0 5-7 11-7 11z"/><circle cx="12" cy="10" r="2.5"/></svg>Palm Beach County, FL</li>
      <li><svg class="ic" viewBox="0 0 24 24"><circle cx="12" cy="12" r="9"/><path d="M12 7v5l3 2"/></svg>24/7 Emergency Service</li>
    </ul></div>
  </div>
  <div class="fbottom"><span>© 2026 Tidewell Heating. All rights reserved.</span><span>Licensed &amp; Insured | ROC #000000</span></div>
</div></footer>

</body>
</html>
```